Tarvil GmbH business card

We Tarvil GmbH based in Switzerland are looking for a business card design. The Fresh Jung, appealing to customers of all kinds. We already have a logo to upload but still a business card. Details: Tarvil GmbH Address: Lindenweg 14b in 9412 Rudolfen. Tel: 41 76 392 00 47, web: Tarvil.ch, E-mail: info@Tarvil.ch Facebook: Tarvil GmbH. I am the Managing Director: Lukas Verholt. On reverse: Title: Transporter and bus rental Gross: Without deposit Super prices
Contact Information for Business Card
Siehe Projektbeschreibung
Requirements
Should not have
- Other pictures

```html
<!DOCTYPE html>
<html lang="en">
<head>
<meta charset="utf-8">
<title>Tarvil GmbH – Business Card</title>
<link href="https://fonts.googleapis.com/css2?family=Lato:wght@400;700;900&display=swap" rel="stylesheet">
<style>
  :root {
    --stage: #222222;
    --navy: #27246a;
    --steel: #7b93b4;
    --ink: #161616;
    --paper: #ffffff;
    --bar-dark: #050505;
  }
  * { margin: 0; padding: 0; box-sizing: border-box; }
  html, body {
    width: 1189px; height: 1200px; overflow: hidden;
    background: var(--stage);
    font-family: "Lato", sans-serif;
  }
  .card {
    position: absolute; left: 171px; width: 856px; height: 487px;
    border-radius: 28px; overflow: hidden;
    box-shadow: 0 3px 6px rgba(0,0,0,.55);
  }
  .card--front { top: 68px; background: var(--navy); }
  .card--back { top: 627px; background: var(--paper); }

  .brand {
    position: absolute; display: flex; align-items: center; gap: 22px;
    color: var(--paper); font-weight: 900; letter-spacing: 1px;
  }
  .brand__mark { width: 78px; height: 78px; background: var(--paper); }
  .card--front .brand {
    left: 50%; top: 50%; transform: translate(-50%, -55%);
    font-size: 64px;
  }

  .back__band {
    position: absolute; left: 0; top: 0; width: 100%; height: 197px;
    background: var(--navy);
  }
  .back__stripe {
    position: absolute; top: 197px; height: 14px; width: 50%;
  }
  .back__stripe--dark { left: 0; background: var(--bar-dark); }
  .back__stripe--light { right: 0; background: var(--steel); }

  .person { position: absolute; left: 44px; top: 74px; color: var(--paper); }
  .person__name { font-size: 29px; font-weight: 700; line-height: 1; letter-spacing: .3px; }
  .person__surname { color: var(--steel); }
  .person__role { font-size: 23px; font-weight: 400; line-height: 1.2; margin-top: 2px; }

  .card--back .brand {
    right: 55px; top: 58px; font-size: 56px; gap: 0;
  }

  .address {
    position: absolute; left: 44px; top: 284px;
    font-size: 23px; line-height: 29px; color: var(--ink);
  }
  .contacts {
    position: absolute; left: 44px; top: 356px; list-style: none;
    font-size: 23px; line-height: 30px; color: var(--ink);
  }
  .contacts li { display: flex; align-items: center; gap: 10px; }
  .contacts svg { width: 24px; height: 20px; fill: var(--steel); }
  .website {
    position: absolute; right: 55px; top: 416px;
    font-size: 23px; color: var(--ink);
  }
  .website__domain { color: var(--steel); }
</style>
</head>
<body>

<section class="card card--front" aria-label="Card front">
  <div class="brand">
    <span class="brand__mark" aria-hidden="true"></span>
    <span class="brand__name">TARVIL GMBH</span>
  </div>
</section>

<section class="card card--back" aria-label="Card back">
  <div class="back__band"></div>
  <div class="back__stripe back__stripe--dark"></div>
  <div class="back__stripe back__stripe--light"></div>

  <div class="person">
    <p class="person__name">LUKAS <span class="person__surname">VERHOLT</span></p>
    <p class="person__role">Managing Director</p>
  </div>

  <div class="brand"><span class="brand__name">TARVIL GMBH</span></div>

  <address class="address" style="font-style:normal">
    Lindenweg 14b<br>
    9412 Rudolfen
  </address>

  <ul class="contacts">
    <li>
      <svg viewBox="0 0 24 20" aria-hidden="true"><path d="M2 7c0-3 5-5 10-5s10 2 10 5l-1 2-5-1V6H8v2L3 9zM6 10h12l2 8H4z"/></svg>
      41 76 392 00 47
    </li>
    <li>
      <svg viewBox="0 0 24 20" aria-hidden="true"><path d="M7 1h10v5H7zM3 7h18v9h-3v-3H6v3H3zM7 14h10v5H7z"/></svg>
      41 76 392 00 48
    </li>
    <li>
      <svg viewBox="0 0 24 20" aria-hidden="true"><path d="M1 3h22v14H1zM3 5l9 7 9-7v2l-9 7-9-7z" fill-rule="evenodd"/></svg>
      info@Tarvil.ch
    </li>
  </ul>

  <p class="website">www.<span class="website__domain">Tarvil</span>.ch</p>
</section>

</body>
</html>
```